Educational clinic needs a new webpage design

I have a relatively new website but I am unhappy with the design. I was hoping the look of it would more match my logo, brochures, business cards, and postcards. The content is good and it's already mobile ready. The designer used square space, which I would like to keep if possible. My website is www.willowgatestudio.com

Target Market(s)

Parents of school age children

Industry/Entity Type

Education

Number of Pages Required

5+ page

Requirements
Must have
• Pictures must depict the diversity of our students. We service all ages, from preschool through college and our students come from varying races.
Should not have
• I try to avoid the word "tutoring" because what we do is so much more. I like the tag line of "results that go beyond traditional tutoring"

```html
<!DOCTYPE html>
<html lang="en">
<head>
<meta charset="utf-8">
<title>Willowgate Studio</title>
<link href="https://fonts.googleapis.com/css2?family=Arimo:wght@400;700&family=Arvo:ital,wght@0,700;1,700&family=Varela+Round&display=swap" rel="stylesheet">
<style>
:root{
  --purple:#6b2d8f;
  --purple-dark:#4f1f70;
  --purple-soft:#9a63b4;
  --green:#92c43d;
  --grey-head:#d8d8d8;
  --grey-band:#f1f1f1;
  --ink:#2b2b2b;
  --white:#ffffff;
}
*{box-sizing:border-box;margin:0;padding:0}
html,body{width:741px;height:1200px;overflow:hidden;background:var(--white)}
body{position:relative;font-family:"Arimo",Arial,sans-serif;color:var(--ink)}
.abs{position:absolute}
.band{position:absolute;left:0;width:741px}

/* header */
.header{top:0;height:68px;background:var(--grey-head)}
.brand{left:116px;top:14px;display:flex;align-items:center;gap:10px}
.brand-dot{width:36px;height:36px;border-radius:50%;background:var(--purple)}
.brand-name{font-family:"Arimo",sans-serif;font-weight:700;font-size:20px;color:var(--purple);letter-spacing:.5px}
.phone-btn{left:466px;top:22px;width:160px;height:32px;background:var(--green);border:1px solid #7fae2f;display:flex;align-items:center;justify-content:center;gap:8px;font-family:"Varela Round",sans-serif;font-size:16px;color:var(--purple);letter-spacing:1.5px}

/* nav */
.nav{top:68px;height:37px;background:var(--purple)}
.nav a{position:absolute;top:0;height:37px;line-height:37px;color:var(--white);font-weight:700;font-size:11.5px;text-decoration:none}
.nav .active{background:var(--purple-dark);padding:0 16px}

/* hero */
.hero{left:117px;top:105px;width:509px;height:279px;background:linear-gradient(135deg,#6f4a85 0%,#7d5a94 40%,#5d3b78 100%)}
.hero-photo{position:absolute;inset:0;background:radial-gradient(ellipse at 30% 60%,rgba(200,180,200,.35),transparent 60%),radial-gradient(ellipse at 80% 30%,rgba(210,160,150,.25),transparent 55%)}
.hero h1{position:absolute;left:0;width:509px;top:18px;text-align:center;font-family:"Arvo",serif;font-weight:700;font-size:29px;color:var(--white);letter-spacing:2px}
.hero .tag{position:absolute;left:0;width:509px;text-align:center;font-family:"Arvo",serif;font-weight:700;font-style:italic;color:#fffbe8;font-size:20px}
.hero .quote{font-style:normal;font-size:21px}
.hero-cta{position:absolute;left:181px;top:144px;width:159px;height:36px;background:var(--green);color:var(--white);font-family:"Varela Round",sans-serif;font-size:22px;text-align:center;line-height:36px;letter-spacing:1px}
.hero-note{position:absolute;left:0;width:509px;top:220px;text-align:center;color:var(--white);font-size:14px;line-height:19px;letter-spacing:.5px}

/* consultation form */
.offer{top:384px;height:42px;background:var(--purple-soft)}
.offer-text{left:120px;top:390px;font-family:"Varela Round",sans-serif;font-weight:700;color:var(--white);font-size:12px;line-height:15.5px;letter-spacing:.3px}
.field{top:393px;width:106px;height:25px;background:var(--white);border-radius:3px;font-family:"Varela Round",sans-serif;font-size:10px;color:#666;padding:7px 10px}
.get-started{left:538px;top:393px;width:82px;height:25px;background:var(--green);border-radius:3px;color:var(--white);font-family:"Varela Round",sans-serif;font-size:12px;text-align:center;line-height:25px}

/* feature rows */
.features{background:var(--grey-band)}
.feature{position:absolute;width:160px;text-align:center}
.feature-icon{width:26px;height:26px;margin:0 auto;border-radius:3px}
.feature h3{font-weight:400;font-size:10px;margin-top:9px;color:#222}
.feature p{font-size:6px;line-height:9.6px;color:#444;margin:3px auto 0;width:118px;height:29px}
.see-more{display:inline-block;margin-top:3px;padding:0 6px;height:13px;line-height:13px;background:var(--purple);color:var(--white);font-family:"Varela Round",sans-serif;font-size:8.5px;border-radius:2px}
.see-more.on{background:var(--green)}
.divider{position:absolute;width:1px;height:38px;background:#c9c9c9}

/* speciality */
.speciality h2{position:absolute;left:0;width:741px;top:574px;text-align:center;font-weight:400;font-size:18px;color:#222}
.speciality p{position:absolute;left:112px;width:517px;top:595px;text-align:center;font-size:10.9px;line-height:16px;color:#333}
.join{position:absolute;left:290px;top:667px;width:158px;height:37px;background:var(--purple);border:1px solid var(--purple-dark);color:var(--white);font-family:"Arvo",serif;font-weight:700;font-style:italic;font-size:21px;text-align:center;line-height:36px;letter-spacing:1px}

/* testimonial */
.avatar{left:117px;top:860px;width:152px;height:152px;border-radius:50%;background:#bcbcbc;border:3px solid #ececec;box-shadow:0 0 0 1px #bbb}
.story{left:315px;width:312px;text-align:center;font-family:"Varela Round",sans-serif}
.story h2{font-weight:400;font-size:14.5px;letter-spacing:.8px;color:#222}
.story .sub{font-size:8.6px;color:#333;margin-top:2px;letter-spacing:.3px}
.story blockquote{text-align:left;margin:29px 0 0 8px;width:300px;font-size:9.6px;line-height:13px;color:#333}
.who{left:422px;top:962px;width:112px;text-align:center;font-family:"Varela Round",sans-serif;font-style:italic;font-size:9px;line-height:13px;color:#333}
.dots{left:457px;top:990px;display:flex;gap:6px}
.dots i{width:8px;height:8px;border-radius:50%;border:1.5px solid var(--green)}
.dots i.on{background:var(--purple);border-color:var(--purple)}

/* subscribe */
.subscribe{top:1034px;height:37px;background:var(--green)}
.sub-input{left:234px;top:1041px;width:201px;height:23px;background:var(--white);border:1px solid #ccc;font-family:"Varela Round",sans-serif;font-size:11.5px;color:#888;padding:4px 7px;letter-spacing:.5px}
.sub-btn{left:445px;top:1041px;width:89px;height:23px;background:var(--purple);color:var(--white);font-family:"Varela Round",sans-serif;font-size:13px;text-align:center;line-height:23px;letter-spacing:1px}

/* footer */
.footer{top:1071px;height:110px;background:var(--purple)}
.foot-nav{left:116px;top:1090px;color:var(--white)}
.foot-nav h4{font-family:"Varela Round",sans-serif;font-weight:400;font-size:10px;letter-spacing:.6px;margin-bottom:10px}
.foot-nav a{display:block;color:var(--white);text-decoration:none;font-weight:700;font-size:8.4px;line-height:10.2px}
.founder{left:330px;top:1090px;width:296px;text-align:right;color:var(--white);font-size:6.8px}
.founder .lead{font-style:italic;font-weight:700}
.founder .words{margin-top:7px;font-weight:700;line-height:9.6px}
.contact-list{left:360px;top:1133px;color:var(--green);font-family:"Varela Round",sans-serif;font-size:7.2px;letter-spacing:.5px}
.contact-list div{display:flex;align-items:center;gap:5px;height:14px}
.keep{left:551px;top:1135px;color:var(--white);font-size:7px;letter-spacing:.3px}
.social{top:1148px;width:21px;height:21px;border-radius:50%;border:1.5px solid var(--white)}
.social.on{border-color:var(--green);background:var(--purple-soft)}
.bottom{top:1181px;height:19px;background:var(--purple-dark);color:var(--white);font-size:6.8px}
.bottom span{position:absolute;top:6px}
</style>
</head>
<body>

<header class="band header"></header>
<div class="abs brand"><span class="brand-dot"></span><span class="brand-name">Willowgate Studio</span></div>
<div class="abs phone-btn">
  <svg width="14" height="16" viewBox="0 0 14 16"><path d="M3 1l3 3-2 2c1 2 3 4 5 5l2-2 3 3-2 3C6 15 0 9 1 3z" fill="var(--purple)"/></svg>
  555-014-287
</div>

<nav class="band nav">
  <a style="left:118px">HOME</a>
  <a style="left:185px">SERVICES</a>
  <a class="active" style="left:254px">SPECIALITY</a>
  <a style="left:366px">PROGRAMS</a>
  <a style="left:461px">PAYMENTS</a>
  <a style="left:557px">CONTACT US</a>
</nav>

<section class="abs hero">
  <div class="hero-photo" role="img" aria-label="Photo of students studying at a desk with notebooks, a coffee mug and a laptop, under a purple tint"></div>
  <h1>RESULTS</h1>
  <div class="tag" style="top:55px">that Go Beyond Traditional Tutoring.</div>
  <div class="tag quote" style="top:86px">“Is school a struggle?”</div>
  <div class="hero-cta">Contact Us</div>
  <div class="hero-note">AT WILLOWGATE,<br>WE’RE HAPPY TO HEAR FROM YOU<br>WITH QUESTIONS.</div>
</section>

<div class="band offer"></div>
<div class="abs offer-text">Get $50.00 consultation for<br>free for first time clients</div>
<div class="abs field" style="left:315px">Your name</div>
<div class="abs field" style="left:426px">Email</div>
<div class="abs get-started">Get Started</div>

<section class="band features" style="top:426px;height:130px">
  <div class="feature" style="left:90px;top:12px">
    <div class="feature-icon" style="background:#8a7a6a" role="img" aria-label="Graduate teacher icon"></div>
    <h3>WHAT WE DO</h3>
    <p>Since 2004, we have been helping families with their educational needs. We are more than passionate ...</p>
    <span class="see-more">see more</span>
  </div>
  <div class="divider" style="left:263px;top:34px"></div>
  <div class="feature" style="left:290px;top:12px">
    <div class="feature-icon" style="background:#2f9a6a" role="img" aria-label="Chalkboard with math icon"></div>
    <h3>HOW CAN WE HELP</h3>
    <p>At our studio our primary goal is to find out the underlying cause of why a student may not be doing well in ...</p>
    <span class="see-more on">see more</span>
  </div>
  <div class="divider" style="left:463px;top:34px"></div>
  <div class="feature" style="left:478px;top:12px">
    <div class="feature-icon" style="background:#c94a3a" role="img" aria-label="Row of books icon"></div>
    <h3>EXAM PREPARATION</h3>
    <p>More than two million students take college entry exams each year, making it tough to be accepted into the best colleges and</p>
    <span class="see-more">see more</span>
  </div>
</section>

<section class="speciality">
  <h2>SPECIALITY PROGRAMS</h2>
  <p>A screening can help determine a student's strengths, weaknesses and academic level. This can include academic testing or screenings forweaknesses in visual perception, auditory processing or ADHD. Call and schedule a FREE consultation today at (555) 014-2870 to find out what programs would best suit your child's needs.</p>
  <div class="join">Join Now!</div>
</section>

<section class="band features" style="top:716px;height:122px">
  <div class="feature" style="left:93px;top:12px">
    <div class="feature-icon" style="background:#8a8f99" role="img" aria-label="Microscope icon"></div>
    <h3>RESOURCES</h3>
    <p>Our resources are huge number. There is good number of resources are verious typo and nature ...</p>
    <span class="see-more">see more</span>
  </div>
  <div class="divider" style="left:263px;top:32px"></div>
  <div class="feature" style="left:291px;top:12px">
    <div class="feature-icon" style="background:#6a6f7a" role="img" aria-label="Scissors icon"></div>
    <h3>F&amp;Q</h3>
    <p style="width:160px">Q: What is Dyslexia<br>A: Dyslexia affects 1 in 10 individuals, many of whom remain undiagnosed and receive little or no intervention ...</p>
    <span class="see-more">see more</span>
  </div>
  <div class="divider" style="left:463px;top:32px"></div>
  <div class="feature" style="left:478px;top:12px">
    <div class="feature-icon" style="background:#a0674a" role="img" aria-label="Classroom desk icon"></div>
    <h3>SUMMER SESSION</h3>
    <p>Besides our regular programs, we will be adding group classes for the summer. Our reading track is designed to be done in small groups ...</p>
    <span class="see-more">see more</span>
  </div>
</section>

<div class="abs avatar" role="img" aria-label="Portrait photo of the quoted parent"></div>
<div class="abs story" style="top:856px">
  <h2>Technique of the success story.</h2>
  <div class="sub">Thousand have joined success joined us. Find out their opinion.</div>
  <blockquote>“Lorem ipsum dolor sit amet, consectetur adipisicing elit, sed do eiusmod tempor incididunt ut labore et dolore magnaaliqua. Ut enim ad minim veniam, quis &nbsp;labore”</blockquote>
</div>
<svg class="abs" style="left:414px;top:964px" width="16" height="26" viewBox="0 0 16 26"><path d="M13 2L3 13l10 11" fill="none" stroke="#555" stroke-width="1.5"/></svg>
<div class="abs who">Whitaker<br>New yourk, USA.</div>
<svg class="abs" style="left:526px;top:964px" width="16" height="26" viewBox="0 0 16 26"><path d="M3 2l10 11L3 24" fill="none" stroke="#555" stroke-width="1.5"/></svg>
<div class="abs dots"><i class="on"></i><i></i><i></i><i></i></div>

<div class="band subscribe"></div>
<div class="abs sub-input">Your Email address</div>
<div class="abs sub-btn">Subscribe</div>

<footer class="band footer"></footer>
<div class="abs foot-nav">
  <h4>Quick Navigation</h4>
  <a>HOME</a><a>SERVICES</a><a>SPECIALITY</a><a>PROGRAMS</a><a>PAYMENTS</a><a>CONTACT US</a>
</div>
<div class="abs founder">
  <div class="lead">A WORD FROM — Marian Holloway, Founder, Willowgate Studio.</div>
  <div class="words">“I try to have a solution for every parent who walks through our doors,<br>and I look forward to helping many more students in the future.”</div>
</div>
<div class="abs contact-list">
  <div><svg width="10" height="8" viewBox="0 0 10 8"><rect x=".5" y=".5" width="9" height="7" fill="none" stroke="var(--green)"/><path d="M.5.5L5 4.5 9.5.5" fill="none" stroke="var(--green)"/></svg>info@willowgatestudio.com</div>
  <div><svg width="10" height="11" viewBox="0 0 10 11"><path d="M5 10C2 6 1 5 1 4a4 4 0 018 0c0 1-1 2-4 6z" fill="none" stroke="var(--green)"/><circle cx="5" cy="4" r="1.4" fill="var(--green)"/></svg>418 Linden Row, Maple Falls, OR 97012</div>
  <div><svg width="10" height="11" viewBox="0 0 14 16"><path d="M3 1l3 3-2 2c1 2 3 4 5 5l2-2 3 3-2 3C6 15 0 9 1 3z" fill="var(--green)"/></svg>555-014-2870</div>
</div>
<div class="abs keep">KEEP CONECTED</div>
<div class="abs social" style="left:552px"></div>
<div class="abs social on" style="left:578px"></div>
<div class="abs social" style="left:604px"></div>

<div class="band bottom">
  <span style="left:116px">Copyright@willowgatestudio</span>
  <span style="left:404px">Company Information</span>
  <span style="left:499px">Term &amp; Condition</span>
  <span style="left:575px">Privacy Policy</span>
</div>

</body>
</html>
```